Plant Based, Environmentally SAFE Chemistry Business requires corporate standards covering all facet

Tallwood Fuelworks is a Canadian based manufacturer and distributor of proprietary chemical formulations made entirely from domestically grown ingredients. These chemicals are non-toxic, non-caustic, contain no VOC's, will readily biodegrade to their natural state within 28 days, are non-corrosive and non-flammable. They carry an enviable 0-0-0-0 hazard rating and are safe for humans, pets and the environment.
We need a corporate design which includes all forms of marketing materials including business cards, stationery, brochures, case studies, power point standards, product labels and signage.
Corporate standards will include corporate colours matching the corporate logo (Green). Designs will be strong and bold but communicate the environmentally sensitive nature of the products we market.
We have attached corporate logos as well as previous efforts to create a standard for collateral literature and case studies as examples of previous attempts which we are not happy with.
The final designs should be formatted in such a way that Tallwood staff are able to change copy, wording and photos on the body of the brochure without the need of an artist or special effort. If special software is needed to accomplish this, that will need to be specified.
For more information on the company view www.tallwoodfuelworks.ca

Target Market(s)

Oil & Gas Industry, Marine & Aviation & Hospitality Industry

Industry/Entity Type

Chemical Product

Font styles to use
Sans Serif

Colors

Designer to choose colors to be used in the design.

Requirements
Must have
• Include standards for business card, letterhead, 1 page brochure, case studies of 3 - 5 pages, basic standard power point background, product label which can be adjusted for change of product type and volumes in container. Common theme throughout.
Nice to have
• I am open to suggestions. Looking for strong theme which denotes a solid corporation..
• Corporate logo colours are green but is not absolutely essential that the theme be only green. Can incorporate several colours if it compliments the basic logo.
Should not have
• Do not want to have a rainbow of colours or be flashy. Should look like a solid responsible corporation

```html
<!DOCTYPE html>
<html lang="en">
<head>
<meta charset="utf-8">
<title>Tallwood Fuelworks — Stationery Standards</title>
<link href="https://fonts.googleapis.com/css2?family=Raleway:wght@400;500;600&display=swap" rel="stylesheet">
<style>
  :root{
    --bg:#939598;
    --green:#3a9545;
    --green-soft:#4ea553;
    --ink:#3b3b3b;
    --rule:#58595b;
    --paper:#ffffff;
    --photo-sky:#4a5660;
    --photo-glow:#d9731c;
    --photo-ground:#0d0d0d;
  }
  *{box-sizing:border-box;margin:0;padding:0}
  html,body{width:1200px;height:870px;overflow:hidden;background:var(--bg);font-family:"Raleway",sans-serif;color:var(--ink)}
  .canvas{position:relative;width:1200px;height:870px}
  .sheet{position:absolute;background:var(--paper);box-shadow:0 1px 3px rgba(0,0,0,.25);overflow:hidden}

  .wordmark{display:flex;align-items:center;gap:5px;font-weight:600;color:var(--ink);white-space:nowrap;text-transform:uppercase}
  .wordmark .dot{background:var(--green);display:block}

  .footer-rule{position:absolute;left:0;right:0;height:3px;background:var(--rule)}
  .footer-rule::after{content:"";position:absolute;right:0;top:-1px;width:18%;height:5px;background:var(--green)}

  .contact-row{position:absolute;display:flex;gap:10px;font-size:6px;color:var(--ink);white-space:nowrap;align-items:center}
  .contact-row span{display:flex;align-items:center;gap:3px}
  .contact-row i{display:block;width:6px;height:6px;background:var(--green);border-radius:1px}

  /* business cards */
  .card-front{left:74px;top:210px;width:145px;height:82px}
  .card-front .wordmark{position:absolute;left:0;right:0;top:36px;justify-content:center;font-size:7px}
  .card-front .wordmark .dot{width:6px;height:6px}
  .card-front .url{position:absolute;left:0;right:0;top:68px;text-align:center;font-size:3.6px;letter-spacing:.5px;color:var(--green)}
  .card-front .footer-rule{top:76px;height:2px}

  .card-back{left:230px;top:210px;width:145px;height:82px;background:var(--green);color:#fff}
  .card-back .title{position:absolute;left:9px;top:37px;font-size:6px;font-weight:600}
  .card-back .role{position:absolute;left:34px;top:44px;font-size:3px;letter-spacing:.4px}
  .card-back .divider{position:absolute;left:74px;top:22px;width:1px;height:32px;background:rgba(255,255,255,.5)}
  .card-back ul{position:absolute;left:80px;top:22px;list-style:none;font-size:3.4px;line-height:7.6px}
  .card-back li{display:flex;align-items:center;gap:3px}
  .card-back li i{display:block;width:4px;height:4px;background:#fff;border-radius:1px}
  .card-back .footer-rule{top:76px;height:2px;background:#4a4a4a}
  .card-back .footer-rule::after{background:#fff}

  /* envelope */
  .envelope{left:444px;top:79px;width:374px;height:214px;background:transparent;box-shadow:none;overflow:visible}
  .envelope .flap{position:absolute;left:0;top:0;width:374px;height:48px;background:var(--green);border-radius:18px 18px 0 0;color:#fff;font-size:7px;letter-spacing:.6px;text-align:center;padding-top:18px}
  .envelope .flap span{display:inline-block;transform:rotate(180deg)}
  .envelope .body{position:absolute;left:0;top:48px;width:374px;height:166px;background:var(--paper);box-shadow:0 1px 3px rgba(0,0,0,.25)}
  .envelope .wordmark{position:absolute;left:13px;top:30px;font-size:8px}
  .envelope .wordmark .dot{width:7px;height:7px}
  .envelope .contact-row{left:11px;top:140px}
  .envelope .footer-rule{top:154px}

  /* letterhead */
  .letterhead{left:69px;top:315px;width:343px;height:485px}
  .letterhead .wordmark{position:absolute;left:0;right:0;top:41px;justify-content:center;font-size:10px}
  .letterhead .wordmark .dot{width:8px;height:8px}
  .letterhead .contact-row{left:14px;top:462px}
  .letterhead .footer-rule{top:475px}

  /* presentation folder */
  .folder{left:444px;top:315px;width:687px;height:485px}
  .folder .panel-left{position:absolute;left:0;top:0;width:344px;height:485px;background:var(--green)}
  .folder .panel-left .contact-row{left:44px;top:459px;color:#fff}
  .folder .panel-left .contact-row i{background:#fff}
  .folder .panel-right{position:absolute;left:344px;top:0;width:343px;height:485px}
  .folder .masthead{height:129px;display:flex;align-items:center;justify-content:center;padding-top:36px}
  .folder .masthead .wordmark{font-size:17px;gap:8px}
  .folder .masthead .wordmark .dot{width:13px;height:13px}
  .folder .photo{position:absolute;left:0;top:129px;width:343px;height:356px;
    background:linear-gradient(180deg,var(--photo-sky) 0%,#5c5a55 45%,var(--photo-glow) 68%,#3a1d0a 74%,var(--photo-ground) 80%,var(--photo-ground) 100%)}
  .folder .welcome{position:absolute;left:0;right:0;top:411px;text-align:center;padding-left:40px;line-height:1}
  .folder .welcome .big{display:block;color:#fff;font-size:32px;font-weight:400;letter-spacing:1px}
  .folder .welcome .small{display:block;color:var(--green-soft);font-size:13px;font-weight:400;margin-top:3px}
  .folder .footer-rule{top:476px}
</style>
</head>
<body>
<main class="canvas">

  <section class="sheet card-front" aria-label="Business card front">
    <div class="wordmark"><b class="dot"></b>Tallwood Fuelworks</div>
    <div class="url">www.tallwoodfuelworks.ca</div>
    <div class="footer-rule"></div>
  </section>

  <section class="sheet card-back" aria-label="Business card back">
    <div class="title">TITLE NAME LOREM</div>
    <div class="role">JOB TITLE</div>
    <div class="divider"></div>
    <ul>
      <li><i></i>12 Cedar Row Calgary AB</li>
      <li><i></i>+1 403 555 0140</li>
      <li><i></i>+1 403 555 0141</li>
      <li><i></i>info@tallwoodfuelworks.ca</li>
      <li><i></i>www.tallwoodfuelworks.ca</li>
    </ul>
    <div class="footer-rule"></div>
  </section>

  <section class="sheet envelope" aria-label="Envelope">
    <div class="flap"><span>www.tallwoodfuelworks.ca</span></div>
    <div class="body">
      <div class="wordmark"><b class="dot"></b>Tallwood Fuelworks</div>
      <div class="contact-row">
        <span><i></i>Lorem ipsum dolor sit amet</span>
        <span><i></i>+00 0000 0000 00</span>
        <span><i></i>info@tfw.ca</span>
        <span><i></i>www.tfw.ca</span>
      </div>
      <div class="footer-rule"></div>
    </div>
  </section>

  <section class="sheet letterhead" aria-label="Letterhead">
    <div class="wordmark"><b class="dot"></b>Tallwood Fuelworks</div>
    <div class="contact-row">
      <span><i></i>Lorem ipsum dolor sit amet</span>
      <span><i></i>+00 0000 0000 00</span>
      <span><i></i>info@tfw.ca</span>
      <span><i></i>www.tfw.ca</span>
    </div>
    <div class="footer-rule"></div>
  </section>

  <section class="sheet folder" aria-label="Presentation folder">
    <div class="panel-left">
      <div class="contact-row">
        <span><i></i>Lorem ipsum dolor sit amet</span>
        <span><i></i>+00 0000 0000 00</span>
        <span><i></i>info@tfw.ca</span>
        <span><i></i>www.tfw.ca</span>
      </div>
    </div>
    <div class="panel-right">
      <div class="masthead">
        <div class="wordmark"><b class="dot"></b>Tallwood Fuelworks</div>
      </div>
      <div class="photo" role="img" aria-label="Photograph of an oil pumpjack silhouetted against a sunset over flat land"></div>
      <div class="welcome">
        <span class="big">WELCOME</span>
        <span class="small">TO TALLWOOD FUELWORKS</span>
      </div>
    </div>
    <div class="footer-rule"></div>
  </section>

</main>
</body>
</html>
```